Specialized Personal Trainer Needs a Business Card Design

I need a business card design for my personal training business called Tall Oak Fitness. I have my Human Kinetics degree in Exercise Science from the Halvern Ridge University as well as an extra certification from NBEP (National Board of Exercise Practice). I work as a Cardiac Rehab Exercise Specialist and personal trainer giving specialized exercise prescriptions to those that have different heart conditions as well as work with the general population in weight loss, strength and conditioning, getting/staying fit.
Updates

I decided that I wanted a logo (as I did not have one before I submitted my project for a business card) so I am submitting a project to get a logo done and then I will decide on a business card, hopefully being able to use one of the designs already submitted.  My apologies for doing this backwards.  I am new to this so I appreciate your patience.

Thank you.

Hi, I have just created a project for a logo design (I realized I needed a logo and I should've done that first..oops!), please feel free to participate.  Once I receive a logo I like I will finalize my business card project and hopefully incorporate it into one of your business card designs. 

Thank you!

Target Market(s)

Business professionals

Industry/Entity Type

Personal Trainer

Requirements
Must have
• My name with my info:
Celia R. Dunhill (BHK)
NBEP Certified Clinical Exercise Specialist & Personal Trainer
celia.dunhill@talloakfitness.example
Cell: 604-358-4170

Please make it double sided.
Nice to have
• An image that represents cardiac and general fitness training.

```html
<!DOCTYPE html>
<html lang="en">
<head>
<meta charset="utf-8">
<title>Tall Oak Fitness – Business Card</title>
<link rel="stylesheet" href="https://fonts.googleapis.com/css2?family=Mulish:wght@300;700&display=swap">
<style>
  :root {
    --backdrop: #e7e3dc;
    --card: #f7f7f5;
    --ink: #1c1c1c;
    --ink-soft: #2e2e2e;
    --brand-red: #d8232a;
  }
  * { box-sizing: border-box; margin: 0; padding: 0; }
  html, body {
    width: 1200px;
    height: 900px;
    overflow: hidden;
    background: var(--backdrop);
  }
  .canvas {
    position: relative;
    width: 1200px;
    height: 900px;
  }
  .card {
    position: absolute;
    left: 110px;
    top: 170px;
    width: 980px;
    height: 560px;
    background: var(--card);
    box-shadow: 0 10px 30px rgba(0,0,0,0.12);
    overflow: hidden;
  }
  .business-name {
    position: absolute;
    left: 44px;
    top: 56px;
    font-family: "Mulish", sans-serif;
    font-weight: 700;
    font-size: 56px;
    line-height: 70px;
    color: var(--ink);
  }
  .accent-band {
    position: absolute;
    left: 0;
    top: 170px;
    width: 100%;
    height: 64px;
    background: var(--brand-red);
  }
  .holder {
    position: absolute;
    left: 44px;
    top: 290px;
    font-family: "Mulish", sans-serif;
    color: var(--ink);
  }
  .holder__name {
    font-size: 34px;
    font-weight: 700;
    line-height: 44px;
  }
  .holder__title {
    margin-top: 4px;
    font-size: 24px;
    font-weight: 300;
    line-height: 32px;
    color: var(--ink-soft);
  }
  .contact {
    position: absolute;
    left: 44px;
    top: 420px;
    list-style: none;
    font-family: "Mulish", sans-serif;
    font-weight: 300;
    font-size: 30px;
    color: var(--ink);
  }
  .contact__item {
    display: flex;
    align-items: center;
    gap: 16px;
    line-height: 46px;
  }
  .contact__icon { width: 22px; height: 22px; flex: none; }
</style>
</head>
<body>
<main class="canvas">
  <article class="card">
    <h1 class="business-name">Tall Oak Fitness</h1>
    <div class="accent-band"></div>

    <div class="holder">
      <p class="holder__name">Celia R. Dunhill (BHK)</p>
      <p class="holder__title">NBEP Certified Clinical Exercise Specialist &amp; Personal Trainer</p>
    </div>

    <ul class="contact">
      <li class="contact__item">
        <svg class="contact__icon" viewBox="0 0 24 24" aria-hidden="true">
          <path d="M6.6 2.5l3 3.2-1.9 2.4c1.2 2.7 3.4 4.9 6.2 6.2l2.4-1.9 3.2 3-2 3.6C10.3 18.7 5.3 13.7 3 6.5z" fill="#1c1c1c"/>
        </svg>
        <span>604-358-4170</span>
      </li>
      <li class="contact__item">
        <svg class="contact__icon" viewBox="0 0 24 24" aria-hidden="true">
          <rect x="2" y="5" width="20" height="14" fill="#1c1c1c"/>
          <path d="M2.5 5.5L12 13l9.5-7.5" fill="none" stroke="#f7f7f5" stroke-width="1.6"/>
        </svg>
        <span>celia.dunhill@talloakfitness.example</span>
      </li>
    </ul>
  </article>
</main>
</body>
</html>
```